Q.R. Bright Desk Store

The design is for eCommerce home page but I would like it to complement this site: http://www.qrbrightdesksystems.com/ but... it should also have independence as a standalone site.

The best design will be able to effectively mix corporate with a high quality small business consumer feel. It should be completely custom design, not a template look or feel. I want the users to get the feeling that this is the place to go for buying tech for business. We sell the same products as Vantrel.

You can be creative as you wish, as long as the elements of a great eCommerce site are present.

I would like your 'design' to blow these away:
http://www.buying.zorvex.com/
mivoland.com
http://www.vantrel.com/

Here are references:
Call to action
http://trabelwise.com/us/blog/48173-seven-tips-for-designing-an-effective-ecommerce-call-to-action

Effective Ecommerce design
http://www.plov.com/ss/7-tips-for-effective-e-commerce#0

91 points of ecommerce
http://dreb.com/blog/holygrail-of-ecommerce-conversion-optimization-91-points-checklist

UPDATE 07/11/2013:

Please look at the category sample png files. I see already many people are using the main menu from qrbrightdesksystems.com and I do not mind your creativiety, but this is an eCommerce store and people need a menu to get to the categories and/or product types. I don't want to limit anyone creativity by the png samples. I'm also not using them to show I like them in any particular way or form, just that it's needed, whether it's a button (dropdown of course) that says 'Categories' or 'Products, whether it an accordion, horizontal or vertical.

Thanks

UPDATE 07/12/2013:

Please find other use of space that has been used for About Us paragraph (if you've added it to the page). About Us should have it's own page and the purpose of the design should be to sell products (and some services as products). Please put a link or some other creative method to lead users to the About Us page.

Reason: I've raised the award, including 1st, 2nd, and 3rd place and participation payments so I will also extend 7 days. Thanks!

I've updated the product brief. Please scroll down to where it says: UPDATE 07/11/2013

Thanks!

UPDATE 07/12/2013:

Please find other use of space that has been used for About Us paragraph (if you've added it to the page).  About Us should have it's own page and the purpose of the design should be to sell products (and some services as products). Please put a link or some other creative method to lead users to the About Us page if you must but not on the real estate of the page.

Thanks!

Added updates to the brief 7/14/2013.

Thanks!

The voting is in and the project is complete.  Thanks everyone for joining, all of those who participated are truly amazingly talented. But, there were only 3 prizes.  I will be having further projects down the line to develop other pages to this site after the initial implementation is completed.  I truly would like to have you all back. 

- Thank you.

Target Market(s)

corporate decision-makers AND small business consumers

Industry/Entity Type

Small Business

Requirements
Must have
• Call to action.
Openness (non-clutter).

These elements:
Search box
Logo
Tagline
Telephone number
Contact details
Address
My account / sign in
Shopping basket / checkout link
Latest offers
Promotional area
Email sign up
Delivery information
About us
Link to press office / corporate site
Terms and conditions
Sitemap for the footer.
Delivery offers: free
Personalized recommendations
Social media links
Accepted payment methods
Link to blog or community section
Change language / country

http://freshnotesblog.kelvarant.com/sales-leads-landing-page/

UPDATE 07/14/2013
Category Menu. This can be a dropdown, horizontal, vertical, etc. But shoppers need to know how to get to the products they want to buy.
Nice to have
• Trustmarks
Blog/Blog link

UPDATE 07/12/2013:
Make the footer useful.

UPDATE 07/14/2013 (Suggestions of elements to differentiate your designs)

-Quick Shop: A quick buy module/section: Where a user can put in a SKU number or Model number to quickly add the product to their shopping cart.

-Featured
-Best Sellers
-Specials
-Trending Tags/Tag Cloud
- Activity Stream
- Cross Sell/ Up Sell
- Testimonial
- Social Network Feed
- Live Help
- Feedback/Support/Contact Tab
- Show logged in user (i.e. Welcome, Mark Pell)
Should not have
• The design SHOULD NOT be generic like this:

http://www.artflock.com/design/52392
http://www.pelicanvault.com/

The page should not feel over cluttered. It should not have low quality icons or design elements. Navigation should not be hard to discover or confusing.

```html
<!DOCTYPE html>
<html lang="en">
<head>
<meta charset="utf-8">
<title>Q.R. Bright Desk Store</title>
<link href="https://fonts.googleapis.com/css2?family=Open+Sans:ital,wght@0,400;0,600;0,700;0,800;1,400&display=swap" rel="stylesheet">
<style>
:root{
  --orange:#f68b33;
  --orange-dark:#e2741d;
  --blue:#3d8fc4;
  --blue-dark:#2a6f9f;
  --blue-deep:#21628f;
  --teal:#3fb3a3;
  --charcoal:#3a3a3a;
  --grey-band:#bdbdbd;
  --grey-light:#efefef;
  --white:#fff;
  --text:#555;
  --footer:#2b2b2b;
  --footer-head:#232323;
  --footer-base:#1c1c1c;
}
*{box-sizing:border-box;margin:0;padding:0}
html,body{width:1065px;height:1200px;overflow:hidden}
body{position:relative;background:var(--white);font-family:"Open Sans",Arial,sans-serif;color:var(--text)}
.abs{position:absolute}

/* header */
.masthead{left:0;top:0;width:1065px;height:118px;background:var(--charcoal);border-top:4px solid var(--orange)}
.logo-box{left:136px;top:14px;width:241px;height:93px;background:#2a2a2a;border-radius:3px;display:flex;align-items:center;padding-left:14px;gap:12px}
.logo-mark{width:44px;height:44px;border-radius:50%;background:var(--orange);flex:none}
.logo-name{font-weight:800;font-size:21px;line-height:22px;color:var(--blue);white-space:nowrap}
.logo-tag{font-size:12px;color:var(--orange);margin-top:4px;font-weight:600}
.help-box{left:497px;top:16px;width:216px;height:92px;background:#2a2a2a;border-radius:3px;padding:13px 0 0 19px}
.help-box h2{font-weight:400;font-size:18px;color:var(--orange)}
.help-row{display:flex;align-items:center;gap:10px;margin-top:6px}
.phone-icon{width:32px;height:32px;background:var(--orange);border-radius:4px;display:flex;align-items:center;justify-content:center}
.help-lines{color:#fff;font-size:14px;line-height:18px}
.help-lines b{font-weight:700}
.account-tab{left:729px;top:0;width:200px;height:27px;background:var(--orange);border-radius:0 0 3px 3px;color:#fff;font-size:12px;font-weight:600;text-align:center;line-height:27px}
.socials{left:793px;top:39px;display:flex;gap:4px}
.soc{width:22px;height:22px;border-radius:3px}
.lang{left:872px;top:39px;width:50px;height:23px;background:#f3f3f3;border-radius:2px}
.search{left:729px;top:74px;width:200px;height:33px;background:#fff;border-radius:2px;font-size:11px;color:#999;line-height:33px;padding-left:16px}
.search-btn{left:890px;top:74px;width:39px;height:33px;background:var(--orange);border-radius:0 2px 2px 0;display:flex;align-items:center;justify-content:center}

/* nav */
.mainnav{left:0;top:118px;width:1065px;height:44px;background:var(--blue)}
.mainnav a,.subnav a{position:absolute;top:0;color:#fff;text-decoration:none;font-size:13.5px;line-height:44px;text-align:center;border-right:1px solid rgba(0,0,0,.12)}
.mainnav a.active{background:var(--blue-deep)}
.nav-drop{left:508px;top:114px;width:44px;height:48px;background:var(--blue-dark);border-radius:3px 3px 0 0}
.subnav{left:0;top:162px;width:1065px;height:40px;background:var(--grey-light)}
.subnav a{color:#666;line-height:40px;font-size:14px;border-right:1px solid #ddd}
.caret{display:inline-block;width:0;height:0;border-left:4px solid transparent;border-right:4px solid transparent;border-top:5px solid currentColor;margin-left:10px;vertical-align:middle}
.basket{left:603px;top:162px;width:176px;height:40px;background:var(--orange);color:#fff;font-size:14px;display:flex;align-items:center;padding-left:18px;gap:22px}
.basket-total{left:779px;top:162px;width:153px;height:40px;background:#f6f6f6;line-height:40px;text-align:center;font-size:15px;color:#333}
.basket-total span{color:var(--blue)}

/* promo */
.promo{left:133px;top:207px;width:604px;height:237px;border:1px solid #ddd;padding:3px}
.promo-photo{width:100%;height:100%;background:linear-gradient(120deg,#8fb2c8 0%,#3e7fae 40%,#cfd6dc 75%,#9aa4ab 100%)}
.promo-card{left:140px;top:245px;width:258px;height:166px;background:rgba(40,40,40,.82)}
.promo-card h1{background:#2a2a2a;color:#fff;font-size:24px;font-weight:700;padding:5px 16px;height:41px}
.promo-card p{color:#eee;font-size:12.5px;line-height:19px;padding:11px 12px 0 14px}
.promo-btn{left:273px;top:373px;width:118px;height:27px;background:var(--blue);color:#fff;font-size:12.5px;line-height:27px;padding-left:10px}
.promo-dots{left:142px;top:411px;width:256px;height:25px;background:#333;display:flex;align-items:center;justify-content:center;gap:3px}
.dot{width:10px;height:10px;background:#fff}
.dot.on{background:var(--orange)}

/* news */
.news-head{left:740px;top:207px;width:191px;height:36px;background:var(--teal);color:#fff;font-size:17px;line-height:36px;padding-left:12px}
.news-item{left:740px;width:191px;height:84px;border-bottom:1px solid #e3e3e3}
.news-day{position:absolute;left:2px;top:3px;width:48px;height:48px;background:var(--blue);color:#fff;font-size:36px;font-weight:600;text-align:center;line-height:48px;letter-spacing:-1px}
.news-mon{position:absolute;left:4px;top:54px;color:var(--blue);font-size:15px}
.news-title{position:absolute;left:59px;top:2px;font-size:13px;color:#333}
.news-text{position:absolute;left:59px;top:20px;font-size:8.8px;line-height:14px;color:#666;width:130px}
.news-text a{color:var(--blue);text-decoration:none}
.news-all{left:740px;top:409px;width:191px;height:35px;background:var(--teal);color:#fff;font-size:13.5px;font-weight:600;text-align:right;line-height:35px;padding-right:15px}

/* products */
.things{left:133px;top:451px;width:604px;height:40px;background:var(--blue);color:#fff;font-size:17px;line-height:40px;padding-left:17px}
.view-toggle{left:663px;top:451px;width:74px;height:40px;background:var(--blue-dark)}
.card{width:197px;height:207px;top:496px;background:#f8f8f8;border:1px solid #eee}
.card-head{height:34px;background:var(--orange);color:#fff;font-size:13px;font-weight:600;text-align:center;line-height:34px}
.card-img{margin:10px auto 0;width:140px;height:105px;background:linear-gradient(#e6e6e6,#bcbcbc);border-radius:3px}
.price{position:absolute;left:8px;top:174px;font-size:13px;color:#999}
.price span{color:var(--blue)}
.price.two{top:161px;font-size:11.5px;line-height:14px}
.price s{color:#999}
.showme{position:absolute;left:92px;top:170px;width:99px;height:30px;background:var(--blue);color:#fff;font-size:12.5px;line-height:30px;padding-left:11px}
.showme i{position:absolute;right:0;top:0;width:28px;height:30px;background:var(--blue-dark);display:flex;align-items:center;justify-content:center}
.plus{width:11px;height:11px;border-radius:50%;background:#fff;position:relative}
.plus:before,.plus:after{content:"";position:absolute;background:var(--blue-dark);left:2.5px;top:4.5px;width:6px;height:2px}
.plus:after{left:4.5px;top:2.5px;width:2px;height:6px}
.card.stub{top:708px;height:51px}
.card.stub .card-head{background:linear-gradient(var(--orange),#fbc79d)}
.more-bar{left:131px;top:759px;width:607px;height:29px;background:var(--blue)}

/* side panels */
.side{left:740px;width:191px;color:#fff;font-size:17px;padding-left:13px}
.testi-head{left:740px;top:495px;width:191px;height:41px;background:#333;color:#fff;font-size:17px;line-height:41px;padding-left:13px}
.testi-body{left:740px;top:536px;width:191px;height:140px;background:#575757;color:#ddd;font-style:italic;font-size:10.5px;line-height:17.5px;padding:7px 12px}
.testi-by{position:absolute;right:10px;bottom:6px;font-style:normal;font-size:10px;color:#fff;font-weight:600}
.moreinfo{left:777px;top:784px;width:154px;height:26px;background:#b7b7b7;color:#fff;font-size:12px;line-height:26px;padding-left:22px;border-radius:3px 3px 0 0}

/* info band */
.band{left:0;top:809px;width:1065px;height:128px;background:var(--grey-band)}
.info{top:817px;width:191px;height:102px;background:#fff}
.info h3{height:30px;background:#6b6b6b;color:#fff;font-size:13.5px;font-weight:600;text-align:center;line-height:30px}
.info p{font-size:9.6px;line-height:14.4px;color:#555;padding:6px 8px}
.trust{left:737px;top:817px;width:193px;height:102px;background:#fff}

/* footer */
.foot-head{left:0;top:937px;width:1065px;height:48px;background:var(--footer-head)}
.foot{left:0;top:985px;width:1065px;height:171px;background:var(--footer)}
.fh{top:950px;color:#fff;font-size:17px}
.qlinks{left:142px;top:988px;width:189px;list-style:none}
.qlinks li{color:#fff;font-size:11px;height:24px;line-height:22px;padding-left:11px;border-bottom:1px solid #474747}
.fp{color:#fff;font-size:10.5px;line-height:16px}
.email{left:348px;top:1078px;width:173px;height:29px;background:#fff;border:2px solid #888;font-size:12px;color:#444;line-height:25px;padding-left:8px}
.email-btn{left:497px;top:1078px;width:24px;height:29px;background:#444;display:flex;align-items:center;justify-content:center}
.cards{left:545px;top:1020px;display:grid;grid-template-columns:repeat(4,40px);gap:4px 4px}
.pay{height:24px;background:#f2f2f2;border-radius:2px;font-size:7.5px;font-weight:600;color:#444;text-align:center;line-height:24px;white-space:nowrap}
.base{left:0;top:1156px;width:1065px;height:44px;background:var(--footer-base);color:#fff;font-size:10px;text-align:right;line-height:28px;padding-right:146px;padding-top:8px}
</style>
</head>
<body>

<header>
  <div class="abs masthead"></div>
  <div class="abs logo-box">
    <span class="logo-mark"></span>
    <div>
      <div class="logo-name">Q.R. BRIGHT<br>DESK SYSTEMS</div>
      <div class="logo-tag">Tagline goes along here</div>
    </div>
  </div>
  <div class="abs help-box">
    <h2>We're Here to Help!</h2>
    <div class="help-row">
      <span class="phone-icon"><svg width="18" height="18" viewBox="0 0 24 24"><path fill="#fff" d="M6.6 10.8a15 15 0 0 0 6.6 6.6l2.2-2.2a1 1 0 0 1 1-.25 11.4 11.4 0 0 0 3.6.57 1 1 0 0 1 1 1V20a1 1 0 0 1-1 1A17 17 0 0 1 3 4a1 1 0 0 1 1-1h3.5a1 1 0 0 1 1 1c0 1.25.2 2.45.57 3.57a1 1 0 0 1-.25 1z"/></svg></span>
      <div class="help-lines"><b>LCL:</b> 212 555 0142<br><b>TF:</b> 888 555 0187</div>
    </div>
  </div>
  <div class="abs account-tab">My account &nbsp;|&nbsp; sign in &nbsp;|&nbsp; Register</div>
  <div class="abs socials">
    <span class="soc" style="background:#3b5a9a"></span>
    <span class="soc" style="background:#7fd0e6"></span>
    <span class="soc" style="background:#f08a24"></span>
  </div>
  <div class="abs lang"><svg width="50" height="23"><rect x="8" y="7" width="13" height="9" fill="#2a5a9e"/><path d="M34 10l4 4 4-4" fill="#888"/><line x1="29" y1="2" x2="29" y2="21" stroke="#ddd"/></svg></div>
  <div class="abs search">Search website....</div>
  <div class="abs search-btn"><svg width="20" height="20" viewBox="0 0 20 20"><circle cx="12" cy="8" r="5.5" fill="none" stroke="#fff" stroke-width="2"/><line x1="8" y1="12" x2="2" y2="18" stroke="#fff" stroke-width="3"/></svg></div>
</header>

<nav class="abs mainnav">
  <a class="active" style="left:136px;width:51px">Home</a>
  <a style="left:187px;width:105px">Small Business</a>
  <a style="left:292px;width:77px">Enterprise</a>
  <a style="left:369px;width:84px">Non-Profit</a>
  <a style="left:578px;width:104px">Go Shopping</a>
  <a style="left:682px;width:58px">Billing</a>
  <a style="left:740px;width:104px">Get Support</a>
  <a style="left:844px;width:88px">Contact Us</a>
</nav>
<div class="abs nav-drop"><svg width="44" height="40"><path d="M18 13l4 4 4-4z" fill="#fff"/></svg></div>

<nav class="abs subnav">
  <a style="left:136px;width:110px">Hardware<span class="caret"></span></a>
  <a style="left:246px;width:104px">Software<span class="caret"></span></a>
  <a style="left:350px;width:130px">IT Resources<span class="caret"></span></a>
  <a style="left:480px;width:123px">Technology<span class="caret"></span></a>
</nav>
<div class="abs basket">
  <svg width="26" height="20" viewBox="0 0 26 20"><path d="M1 2h4l3 11h13l3-8H7" fill="none" stroke="#fff" stroke-width="2.4"/><circle cx="10" cy="17" r="2" fill="#fff"/><circle cx="19" cy="17" r="2" fill="#fff"/></svg>
  <span>My Basket</span><span class="caret" style="margin-left:8px"></span>
</div>
<div class="abs basket-total"><span>0 items</span> &nbsp;: &nbsp;£0.00</div>

<section>
  <div class="abs promo"><div class="promo-photo" role="img" aria-label="Close-up photo of a keyboard with a large blue Solutions key"></div></div>
  <div class="abs promo-card">
    <h1>Promotional area</h1>
    <p>Dut scelerisque diam. Donec pulvinar ultricies sem, vel dapibus eros Maecen as auctor.Etiam at mauris tortor, ut sceler isque diam.</p>
  </div>
  <div class="abs promo-btn">View Product<span style="position:absolute;right:0;top:0;width:25px;height:27px;background:var(--blue-dark);display:flex;align-items:center;justify-content:center"><span class="plus"></span></span></div>
  <div class="abs promo-dots">
    <svg width="12" height="10"><path d="M8 1L3 5l5 4z" fill="#fff"/></svg>
    <span class="dot"></span><span class="dot"></span><span class="dot"></span><span class="dot on"></span>
    <svg width="12" height="10"><path d="M4 1l5 4-5 4z" fill="#fff"/></svg>
  </div>
</section>

<aside>
  <div class="abs news-head">Top News</div>
  <div class="abs news-item" style="top:247px">
    <div class="news-day">04</div><div class="news-mon">Jan 13</div>
    <div class="news-title">Latest news title</div>
    <div class="news-text">Donec pulvinar ultricies sem, vel dapibus eros Mae cenas auctor quam sit am et ante tristique....<a>more</a></div>
  </div>
  <div class="abs news-item" style="top:331px;border:0">
    <div class="news-day">13</div><div class="news-mon">Feb 13</div>
    <div class="news-title">Latest news title</div>
    <div class="news-text">Donec pulvinar ultricies sem, vel dapibus eros Mae cenas auctor quam sit am et ante tristique....<a>more</a></div>
  </div>
  <div class="abs news-all">View all posts</div>
</aside>

<section>
  <div class="abs things">Things you might like...</div>
  <div class="abs view-toggle">
    <svg width="74" height="40">
      <g fill="none" stroke="#cfe3f1" stroke-width="1.5"><rect x="6" y="9" width="7" height="6"/><rect x="15" y="9" width="7" height="6"/><rect x="24" y="9" width="7" height="6"/><rect x="6" y="17" width="7" height="6"/><rect x="15" y="17" width="7" height="6"/><rect x="24" y="17" width="7" height="6"/><rect x="6" y="25" width="7" height="6"/><rect x="15" y="25" width="7" height="6"/><rect x="24" y="25" width="7" height="6"/></g>
      <g fill="#5b9fcc"><rect x="42" y="9" width="5" height="5"/><rect x="49" y="9" width="5" height="5"/><rect x="56" y="9" width="5" height="5"/><rect x="63" y="9" width="5" height="5"/><rect x="42" y="16" width="5" height="5"/><rect x="49" y="16" width="5" height="5"/><rect x="56" y="16" width="5" height="5"/><rect x="63" y="16" width="5" height="5"/><rect x="42" y="23" width="5" height="5"/><rect x="49" y="23" width="5" height="5"/><rect x="56" y="23" width="5" height="5"/><rect x="63" y="23" width="5" height="5"/></g>
    </svg>
  </div>

  <article class="abs card" style="left:133px">
    <div class="card-head">Product name</div>
    <div class="card-img" role="img" aria-label="Flat screen computer monitor"></div>
    <div class="price">Only <span>£300.00</span></div>
    <div class="showme">Show me<i><span class="plus"></span></i></div>
  </article>
  <article class="abs card" style="left:337px">
    <div class="card-head">Product with a long name</div>
    <div class="card-img" role="img" aria-label="Over-ear headphones"></div>
    <div class="price">Only <span>£99.00</span></div>
    <div class="showme">Show me<i><span class="plus"></span></i></div>
  </article>
  <article class="abs card" style="left:540px">
    <div class="card-head">Product name</div>
    <div class="card-img" role="img" aria-label="Laptop computer"></div>
    <div class="price two">Was <s>£9999.00</s><br>Now <span>£999.00</span></div>
    <div class="showme">Show me<i><span class="plus"></span></i></div>
  </article>

  <div class="abs card stub" style="left:133px"><div class="card-head">Product name</div></div>
  <div class="abs card stub" style="left:337px"><div class="card-head">Product with a long name</div></div>
  <div class="abs card stub" style="left:540px"><div class="card-head">Product name</div></div>
  <div class="abs more-bar"><svg width="607" height="29"><path d="M299 18l4 4 4-4z" fill="#fff"/></svg></div>
</section>

<aside>
  <div class="abs side" style="top:451px;height:40px;background:var(--blue);line-height:40px">Go to Shop</div>
  <div class="abs testi-head">Testimonials</div>
  <div class="abs testi-body">Etiam at mauris tortor, ut sceleris-que diam. Donec pulvinar ultricies sem, vel dapibus eros Maecenas auctor.Etiam at mauris tortor, ut scelerisque diam. Donec pulvinar ultricies sem, vel dapibus eros<span class="testi-by">- &nbsp;Tom Hadley</span></div>
  <div class="abs side" style="top:680px;height:41px;background:var(--orange);line-height:41px">My Account</div>
  <div class="abs side" style="top:724px;height:41px;background:var(--blue);line-height:41px">Contact us</div>
  <div class="abs moreinfo">More information<span class="caret" style="margin-left:16px"></span></div>
</aside>

<section>
  <div class="abs band"></div>
  <div class="abs info" style="left:133px"><h3>About us</h3><p>Etiam at mauris tortor, ut scelerisque diam. Donec pulvinar ultricies sem, vel dapibus eros Maecenas auctor.Etiam at mauris tortor, ut scelerisque diam.</p></div>
  <div class="abs info" style="left:337px"><h3>Delivery options : Free</h3><p>Etiam at mauris tortor, ut scelerisque diam. Donec pulvinar ultricies sem, vel dapibus eros Maecenas auctor.Etiam at mauris tortor, ut scelerisque diam.</p></div>
  <div class="abs info" style="left:536px"><h3>Delivery information</h3><p>Etiam at mauris tortor, ut scelerisque diam. Donec pulvinar ultricies sem, vel dapibus eros Maecenas auctor.Etiam at mauris tortor, ut scelerisque diam.</p></div>
  <div class="abs trust">
    <svg width="193" height="102" aria-label="Security and certification badges">
      <rect x="12" y="12" width="66" height="28" rx="4" fill="#e4e4e4"/>
      <rect x="90" y="14" width="90" height="24" rx="4" fill="#dfe9df"/>
      <circle cx="35" cy="71" r="20" fill="#f0c7a8"/>
      <rect x="68" y="55" width="112" height="34" rx="4" fill="#ecd6d6"/>
    </svg>
  </div>
</section>

<footer>
  <div class="abs foot-head"></div>
  <div class="abs foot"></div>
  <div class="abs fh" style="left:143px">Quick links</div>
  <div class="abs fh" style="left:349px">Email Sign up</div>
  <div class="abs fh" style="left:545px">Payment options</div>
  <div class="abs fh" style="left:748px">Contact details</div>

  <ul class="abs qlinks">
    <li>Shop</li><li>Latest offers</li><li>Shopping basket</li><li>Press office / corporate site</li><li>Terms and conditions</li><li style="border:0">Sitemap</li>
  </ul>

  <p class="abs fp" style="left:350px;top:991px;width:160px">Keep up-to-date with all of our latest products and special offers</p>
  <p class="abs fp" style="left:350px;top:1050px">Sign up to our newsletter</p>
  <div class="abs email">Email address</div>
  <div class="abs email-btn"><svg width="8" height="10"><path d="M1 1l5 4-5 4z" fill="#fff"/></svg></div>

  <p class="abs fp" style="left:545px;top:991px">We accept all of the payments below</p>
  <div class="abs cards">
    <span class="pay">Debit</span><span class="pay">Credit</span><span class="pay">Wallet</span><span class="pay">Bank</span>
    <span class="pay">Prepaid</span><span class="pay">Invoice</span><span class="pay">Gift</span><span class="pay">Cash</span>
  </div>

  <p class="abs fp" style="left:746px;top:994px;width:160px;font-size:9.8px">Lorem ipsum dolor sit amet, consectetur adipiscing elit. Proin aliquet, enim quis sagittis rutrum, purus metus posuere nibh, sit</p>
  <p class="abs fp" style="left:746px;top:1074px;font-size:9.8px">info@qrbrightdesksystems.com</p>
  <div class="abs" style="left:746px;top:1102px;color:#fff;font-size:15px">Stay in touch</div>
  <div class="abs socials" style="left:745px;top:1124px">
    <span class="soc" style="background:#3b5a9a"></span>
    <span class="soc" style="background:#7fd0e6"></span>
    <span class="soc" style="background:#f08a24"></span>
  </div>

  <div class="abs base">Copyright 2013 · All rights reserved</div>
</footer>

</body>
</html>
```